Healthy living company needs logo / business card

We are looking for a business identity for our company that operates in the Health and Wellness area.
Our audience is those open to hearing about the links between ill health and chemicals in the home as well as how to boost their health naturally through nutrition. We show people how to eliminate those toxins and share the message with others.
We also work with and mentor people who want to build their own business, share the message and create a leveraged income.
Our business name is: Larkwell
The tag line we have is: Simple Changes ยท Healthy Living
Output for the project is:
Logo and business card design (2 people on the card).
Our perspective is for a modern, natural, simple, clean design (web 2.0 feel) that will appeal to a broad age range and audience. It should feel professional but not formal. It should not seem medical.
The logo should not be a gradient nor overly complex. Colouring should only be one or two colours at most. They can be bright, we are tending to lean towards green for obvious reasons but open to your thoughts.
Simplicity is the key.
The business card needs to be two sided. We like having the logo and card details on the front and then reversed out on the back with the logo and name in white on the colour block.
Please see the attached card brief document about the card content.

```html
<!DOCTYPE html>
<html lang="en">
<head>
<meta charset="utf-8">
<title>Larkwell Business Card</title>
<link rel="stylesheet" href="https://fonts.googleapis.com/css2?family=Open+Sans:wght@300;400&display=swap">
<style>
  :root {
    --backdrop: #221e1c;
    --card-white: #ffffff;
    --brand-green: #86c126;
    --ink: #1f1f1f;
    --on-green: #ffffff;
  }
  * { margin: 0; padding: 0; box-sizing: border-box; }
  html, body {
    width: 1200px; height: 407px; overflow: hidden;
    background: var(--backdrop);
  }
  .canvas { position: relative; width: 1200px; height: 407px; }
  .card { position: absolute; top: 51px; height: 304px; }
  .card--front { left: 38px; width: 556px; background: var(--card-white); color: var(--ink); }
  .card--back { left: 612px; width: 551px; background: var(--brand-green); color: var(--on-green); }

  .contact {
    position: absolute; top: 26px;
    font-family: "Open Sans", sans-serif; font-size: 14.5px; line-height: 21px;
  }
  .contact--first { left: 32px; }
  .contact--second { left: 355px; }

  .brand {
    position: absolute; display: flex; justify-content: center;
  }
  .brand__name {
    display: flex; align-items: center; gap: 10px;
    font-family: "Open Sans", sans-serif; font-weight: 300; line-height: 1;
  }
  .brand__dot { border-radius: 50%; flex: none; }

  .card--front .brand { left: 0; width: 556px; top: 150px; }
  .card--front .brand__name { font-size: 60px; color: var(--ink); }
  .card--front .brand__dot { width: 22px; height: 22px; background: var(--brand-green); }

  .office {
    position: absolute; left: 0; width: 552px; top: 244px; text-align: center;
    font-family: "Open Sans", sans-serif; font-size: 14.5px; line-height: 21px;
  }

  .card--back .brand { left: 30px; width: 240px; top: 128px; }
  .card--back .brand__name { font-size: 48px; color: var(--on-green); }
  .card--back .brand__dot { width: 18px; height: 18px; background: var(--on-green); }

  .benefits {
    position: absolute; left: 292px; top: 37px;
    border-left: 1px solid rgba(255,255,255,0.75);
    padding-left: 11px; list-style: none;
    font-family: "Open Sans", sans-serif; font-size: 15.8px; line-height: 22.4px;
  }
</style>
</head>
<body>
<main class="canvas">
  <section class="card card--front">
    <div class="contact contact--first"><p>Name</p><p>Cell : 000000 000000</p></div>
    <div class="contact contact--second"><p>Name</p><p>Cell : 000000 000000</p></div>
    <div class="brand">
      <div class="brand__name"><span class="brand__dot"></span>Larkwell</div>
    </div>
    <div class="office">
      <p>Off. Phone : 00000000</p>
      <p>E-mail : hello@larkwellhealth.com</p>
    </div>
  </section>

  <section class="card card--back">
    <div class="brand">
      <div class="brand__name"><span class="brand__dot"></span>Larkwell</div>
    </div>
    <ul class="benefits">
      <li>Multiple Streams of Income</li>
      <li>Financial Freedom</li>
      <li>Own my Own Business</li>
      <li>More Time</li>
      <li>Personal Development</li>
      <li>Health and Vitality</li>
      <li>Help Others</li>
      <li>Meet New People</li>
      <li>Retirement Plan</li>
      <li>Leave a Legacy</li>
    </ul>
  </section>
</main>
</body>
</html>
```